4D Hush Little Nest Luxury Ultrasound Billboard

Design a HIGH-END, MODERN billboard for my private prenatal ultrasound studio, 4D Hush Little Nest, located in Pace, Florida.
This billboard will be viewed by drivers traveling at highway speeds, so it must be extremely clean, simple, and readable within 6 seconds.
About My Business
4D Hush Little Nest is a private prenatal ultrasound studio specializing in:
Highest technology 4D/HD Ultrasounds
Early Gender Determination
Pregnancy Confirmation
I have been serving families for nearly 10 years and is known for creating a memorable experience, not just an ultrasound appointment.
Design Style
I DO NOT want:
Flowers
Leaves
Swirls
Glitter
Hearts everywhere
Busy backgrounds
Generic maternity stock graphics
I DO want:
Modern
Luxury
Upscale
Clean
Professional
Eye-catching
Premium medical spa feel
Colors
Use colors from my logo:
LOGO Green ( or a deep green)
Black
White
Soft Gold accents
Images:
Incorporate my professional headshot in a clean, modern way, logo, and the ultrasound images
Text
Keep wording minimal.
Primary Headline ( OPEN TO IDEAS) :
EXAMPLES ( WOULD RATHER SOMETHING MORE CATCHY)
" ADVANCED IMAGING. UNFORGETTABLE MOMENTS"
"MEET YOUR BABY BEFORE BIRTH"
Under headline:
4D Ultrasound • Early Gender • Pregnancy Confirmation
Business Name:
4D Hush Little Nest
Private Prenatal Ultrasound Studio
Phone Number:
850-471-3905
Important
This billboard must be readable in 5–6 seconds from a moving vehicle.
Less text is better.
The phone number and business name must be visible from a distance.
The design should feel like a premium brand that immediately tells expecting parents:
“This is where I go to see my baby.”
Files Provided
Official logo
Headshot
Ultrasound images
Don’t make this look like a medical office billboard.
Make it look like a luxury baby experience billboard. That’s what separates 4D Hush Little Nest from hospitals, OB offices, and all the new studios popping up around you. The emotional connection is what gets moms to book. ❤️
Billboard Size - 10.6” x 36”

```html
<!DOCTYPE html>
<html lang="en">
<head>
<meta charset="utf-8">
<title>4D Hush Little Nest Billboard</title>
<link href="https://fonts.googleapis.com/css2?family=Hind:wght@400;500;600;700&display=swap" rel="stylesheet">
<style>
  :root {
    --page-bg: #e6e8ea;
    --board-white: #f6f6f4;
    --ink: #1f2523;
    --gold: #d2aa3a;
    --sage: #5d6f64;
    --deep-green: #2f5a3c;
    --scan-red: #a85a48;
  }
  * { box-sizing: border-box; margin: 0; padding: 0; }
  html, body {
    width: 1200px; height: 800px; overflow: hidden;
    background: var(--page-bg);
    font-family: "Hind", Arial, sans-serif;
    color: var(--ink);
  }
  .billboard {
    position: absolute; left: 20px; top: 229px;
    width: 1160px; height: 342px;
    background: var(--board-white);
    box-shadow: 0 10px 30px rgba(0,0,0,.18);
    overflow: hidden;
  }
  .headline {
    position: absolute; left: 30px; top: 34px;
    font-weight: 400; font-size: 58px; line-height: 1.06;
    letter-spacing: -0.5px; text-transform: uppercase;
  }
  .headline .accent { color: var(--gold); font-weight: 700; }
  .scan-image {
    position: absolute; left: 30px; top: 232px;
    width: 82px; height: 92px; border-radius: 18px;
    background: radial-gradient(circle at 40% 45%, #d98f76, var(--scan-red) 55%, #5a2a20);
  }
  .services {
    position: absolute; left: 136px; top: 244px;
    list-style: none; font-size: 19px; font-weight: 500; line-height: 1.45;
  }
  .services li::before { content: "• "; }
  .brand {
    position: absolute; left: 500px; top: 70px; width: 300px;
    text-align: center;
  }
  .brand-name {
    color: var(--gold); font-weight: 700; font-size: 38px; line-height: 1.05;
  }
  .brand-tagline {
    margin-top: 14px; color: var(--sage); font-size: 14px; font-weight: 500;
    letter-spacing: 1.2px; text-transform: uppercase;
  }
  .contact {
    position: absolute; left: 500px; top: 232px; width: 300px; text-align: center;
  }
  .contact-label { color: var(--gold); font-size: 15px; font-weight: 600; }
  .contact-number { font-size: 42px; font-weight: 700; letter-spacing: 0.5px; line-height: 1.1; }
  .headshot {
    position: absolute; right: 0; top: 0; width: 330px; height: 100%;
    background: linear-gradient(180deg, #eef0ee 0%, #e1e4e1 35%, #6f8c74 60%, var(--deep-green) 100%);
  }
</style>
</head>
<body>
  <section class="billboard">
    <h1 class="headline">Meet your<br><span class="accent">Baby</span> before<br>birth</h1>

    <div class="scan-image" role="img" aria-label="4D ultrasound image of twins"></div>
    <ul class="services">
      <li>4D Ultrasound</li>
      <li>Early Gender</li>
      <li>Pregnancy Confirmation</li>
    </ul>

    <div class="brand">
      <div class="brand-name">4D Hush Little Nest</div>
      <div class="brand-tagline">Prenatal Ultrasound Studio</div>
    </div>

    <div class="contact">
      <div class="contact-label">Phone:</div>
      <div class="contact-number">850-471-3905</div>
    </div>

    <div class="headshot" role="img" aria-label="Professional headshot of the sonographer in green scrubs beside an ultrasound machine"></div>
  </section>
</body>
</html>
```